Our companies name is The Gilded Ladle and we specialize in craft cupcakes, what I mean by that is that we bake our cupcakes with craft beer and other alcoholic drinks. We are trying to focus on being elegant but at the same time unpretentious. Since we are incorporating beer in our cupcakes we want the business card to have our logo in the front and our information in the back.

Once we select the best design we will provide the contact information to be added. Thank you.

Industry/Entity Type

Business

Font styles to use
Decorative
Script

Requirements
Must have
• Round corners
Should not have
• Square corners

```html
<!DOCTYPE html>
<html lang="en">
<head>
<meta charset="utf-8">
<title>The Gilded Ladle – Business Card</title>
<link rel="stylesheet" href="https://fonts.googleapis.com/css2?family=Playball&family=Great+Vibes&display=swap">
<style>
  :root {
    --backdrop: #4a3c2e;
    --card-black: #0b0b0b;
    --accent-red: #cc2229;
    --paper-white: #ffffff;
    --text-soft: #f2f2f2;
  }
  html, body {
    margin: 0;
    padding: 0;
    width: 1200px;
    height: 858px;
    overflow: hidden;
    background: var(--backdrop);
  }
  .canvas {
    position: relative;
    width: 1200px;
    height: 858px;
    display: flex;
    align-items: center;
    justify-content: center;
    gap: 50px;
  }
  .card {
    position: relative;
    width: 540px;
    height: 309px;
    border-radius: 16px;
    background: var(--card-black);
    overflow: hidden;
    box-shadow: 0 10px 28px rgba(0,0,0,.45);
  }
  /* Info side */
  .card__band {
    position: absolute;
    left: 0;
    bottom: 0;
    width: 62%;
    height: 62px;
    background: var(--accent-red);
    border-top: 5px solid var(--paper-white);
  }
  .brand-seal {
    position: absolute;
    left: 34px;
    top: 140px;
    width: 140px;
    height: 140px;
    border-radius: 50%;
    background: var(--card-black);
    border: 5px solid var(--paper-white);
    display: flex;
    align-items: center;
    justify-content: center;
    text-align: center;
  }
  .brand-name {
    font-family: "Playball", cursive;
    color: var(--paper-white);
    font-size: 24px;
    line-height: 1.05;
    margin: 0;
  }
  .person {
    position: absolute;
    left: 222px;
    top: 26px;
  }
  .person__name {
    font-family: "Playball", cursive;
    color: var(--accent-red);
    font-size: 34px;
    margin: 0;
    line-height: 1;
  }
  .person__role {
    font-family: "Great Vibes", cursive;
    color: var(--text-soft);
    font-size: 16px;
    margin: 3px 0 0 36px;
  }
  .contact {
    position: absolute;
    left: 250px;
    top: 98px;
    font-family: "Great Vibes", cursive;
    color: var(--text-soft);
    font-size: 17px;
    line-height: 1.2;
    word-spacing: 4px;
  }
  .contact__address { margin: 0 0 6px; }
  .contact__list { list-style: none; margin: 0; padding: 0; }
  .contact__item { display: flex; align-items: center; gap: 8px; }
  .contact__icon {
    width: 11px;
    height: 11px;
    border-radius: 2px;
    background: var(--accent-red);
    flex: none;
    display: flex;
    align-items: center;
    justify-content: center;
  }
  /* Logo side */
  .card--logo {
    display: flex;
    align-items: center;
    justify-content: center;
    gap: 16px;
  }
  .logo-dot {
    width: 22px;
    height: 22px;
    border-radius: 50%;
    background: var(--accent-red);
  }
  .card--logo .brand-name { font-size: 46px; }
</style>
</head>
<body>
<main class="canvas">
  <section class="card card--info" aria-label="Business card, contact side">
    <div class="card__band"></div>
    <div class="brand-seal"><p class="brand-name">The Gilded<br>Ladle</p></div>
    <div class="person">
      <p class="person__name">Employee name</p>
      <p class="person__role">Managing Director</p>
    </div>
    <div class="contact">
      <p class="contact__address">Your Address Inc 2nd Lane Ave Harlow Bay,<br>ST 00000</p>
      <ul class="contact__list">
        <li class="contact__item">
          <span class="contact__icon"><svg width="7" height="7" viewBox="0 0 10 10"><path d="M2 1l2 2-1 1.5c.8 1.5 1.5 2.2 3 3L7.5 6l2 2-1.5 1.5C4 9 1 6 .5 1.5z" fill="#fff"/></svg></span>
          (xxx) xxx-xxxx
        </li>
        <li class="contact__item">
          <span class="contact__icon"><svg width="7" height="7" viewBox="0 0 10 10"><rect x="2" y="1" width="6" height="8" rx="1" fill="#fff"/></svg></span>
          xxx xxx xxxx
        </li>
        <li class="contact__item">
          <span class="contact__icon"><svg width="7" height="7" viewBox="0 0 10 10"><circle cx="5" cy="5" r="4" fill="none" stroke="#fff" stroke-width="1.5"/><path d="M1 5h8M5 1v8" stroke="#fff" stroke-width="1"/></svg></span>
          www.yourwebsit.com
        </li>
        <li class="contact__item">
          <span class="contact__icon"><svg width="7" height="7" viewBox="0 0 10 10"><rect x="1" y="2" width="8" height="6" fill="#fff"/><path d="M1 2l4 3 4-3" stroke="#cc2229" fill="none"/></svg></span>
          info@youremail.com
        </li>
      </ul>
    </div>
  </section>

  <section class="card card--logo" aria-label="Business card, logo side">
    <span class="logo-dot"></span>
    <p class="brand-name">The Gilded Ladle</p>
  </section>
</main>
</body>
</html>
```